New Brazilian Craft Brewery Needs a Logo and Label Design.

We need a beer logo and label design for our new brazilian brewery. The brewery name is "MORVELHA" (that means holy in portuguese). The logo should have the words "MORVELHA" and "CERVEJAS ARTESANAIS" (craft beer). We would like a logo and label desings with something about holy theme like an angel drinking beer, a glass with wings, or anything else we are open to any new sugestion. We would like to see projects that are not the same tipical and classic beer desing. We like different, inovating, colorfull desings. Attached the are some old desings just for reference as we want something different.
Craft beer drinkers.
Brewery

```html
<!DOCTYPE html>
<html lang="pt-BR">
<head>
<meta charset="utf-8">
<title>Morvelha — Cerveja Ale Premium</title>
<link href="https://fonts.googleapis.com/css2?family=Tinos:wght@400;700&display=swap" rel="stylesheet">
<style>
  :root {
    --canvas: #ffffff;
    --frame: #c8680c;
    --gold-deep: #d8980f;
    --gold-mid: #e8b21c;
    --gold-light: #f4c936;
    --rule: #b8620c;
    --ink: #2a1a08;
    --paper: #ffffff;
    --glass-red: #a3202a;
    --glass-blue: #5fa9d6;
    --glass-amber: #e8653f;
  }
  * { box-sizing: border-box; margin: 0; padding: 0; }
  html, body { width: 905px; height: 1200px; overflow: hidden; background: var(--canvas); }
  body { position: relative; font-family: "Tinos", "Times New Roman", serif; color: var(--ink); }

  .label {
    position: absolute; left: 24px; top: 354px; width: 857px; height: 492px;
    border: 8px solid var(--frame);
    background: var(--gold-mid);
    overflow: hidden;
  }
  .label__rule {
    position: absolute; inset: 8px; border: 1px solid var(--rule); pointer-events: none;
  }
  .panel { position: absolute; top: 0; bottom: 0; }
  .panel--side {
    background: linear-gradient(90deg, var(--gold-deep) 0%, var(--gold-light) 45%, var(--gold-mid) 75%, var(--gold-deep) 100%);
  }
  .panel--left { left: 0; width: 249px; }
  .panel--center {
    left: 249px; width: 345px;
    background: linear-gradient(90deg, var(--gold-deep) 0%, var(--gold-light) 12%, var(--gold-light) 88%, var(--gold-deep) 100%);
  }
  .panel--right { left: 594px; right: 0; }

  /* Left panel: vertical legal text */
  .legal-box {
    position: absolute; left: 24px; top: 24px; width: 96px; height: 430px;
    border: 2px solid var(--ink);
  }
  .legal {
    position: absolute; left: 94px; top: 0; width: 430px; height: 94px;
    transform-origin: 0 0; transform: rotate(90deg);
    padding: 3px 4px; font-size: 10.2px; line-height: 15px; text-align: justify;
    text-transform: uppercase; letter-spacing: 0.2px;
  }
  .legal__spacer { float: right; width: 0; height: 30px; }
  .legal__blank {
    float: right; clear: right; width: 108px; height: 58px;
    background: var(--paper); border: 1px solid var(--ink); margin-left: 6px;
  }
  .legal strong { font-weight: 700; }
  .style-name {
    position: absolute; left: 142px; top: 160px; width: 180px;
    transform-origin: 0 0; transform: rotate(90deg);
    font-size: 11.5px; font-weight: 700; letter-spacing: 0.5px; white-space: nowrap;
  }

  /* Center panel */
  .brand {
    position: absolute; left: 0; right: 0; top: 84px; text-align: center;
    font-size: 38px; line-height: 40px; font-weight: 700; letter-spacing: 1px; color: var(--ink);
  }
  .brand__dot {
    display: inline-block; width: 9px; height: 9px; border-radius: 50%;
    background: var(--ink); vertical-align: middle; margin-right: 10px;
  }
  .brand__tagline {
    position: absolute; left: 0; right: 0; top: 128px; text-align: center;
    font-size: 13px; line-height: 15px; letter-spacing: 1.2px; color: var(--ink);
  }
  .emblem {
    position: absolute; left: 44px; top: 172px; width: 262px; height: 262px;
  }
  .volume, .abv { position: absolute; top: 450px; font-size: 13px; }
  .volume { left: 42px; }
  .abv { right: 36px; }

  /* Right panel */
  .maker {
    position: absolute; left: 65px; top: 27px; width: 166px;
    font-size: 9.6px; line-height: 10.5px; text-transform: uppercase; text-align: justify;
    text-align-last: justify;
  }
  .quote {
    position: absolute; left: 65px; top: 68px; width: 166px; height: 52px;
    background: var(--paper); border: 2px solid var(--ink); border-radius: 6px;
    padding: 4px 8px; font-size: 9.4px; line-height: 12.5px; text-align: justify; text-align-last: justify;
  }
  .body-copy { position: absolute; left: 65px; top: 152px; width: 166px; }
  .body-copy p { margin-bottom: 17px; }
  .body-copy span {
    display: block; font-size: 11px; line-height: 17.2px; height: 17.2px;
    text-align: justify; text-align-last: justify; text-transform: uppercase; white-space: nowrap;
  }
</style>
</head>
<body>
  <section class="label">
    <div class="panel panel--side panel--left">
      <div class="legal-box">
        <div class="legal">
          <span class="legal__spacer"></span><span class="legal__blank"></span>
          <strong>Ingredientes:</strong> água, malte de cevada, açúcar de cana, lúpulo e leveduras. Fabricada e engarrafada por Cervejaria Morvelha Ltda. Não congelar. Conservar em local fresco e arejado. Aprecie com moderação. Proibida venda para menores de 18 anos. Indústria brasileira. Contém glúten.
        </div>
      </div>
      <div class="style-name">CERVEJA ALE PREMIUM</div>
    </div>

    <div class="panel panel--center">
      <div class="brand"><span class="brand__dot"></span>MORVELHA</div>
      <div class="brand__tagline">CERVEJAS ARTESANAIS</div>
      <svg class="emblem" viewBox="0 0 260 260" role="img" aria-label="Stained-glass emblem of a beer mug in a round window">
        <defs>
          <radialGradient id="glass" cx="50%" cy="50%" r="50%">
            <stop offset="0%" stop-color="#f2d94a"/>
            <stop offset="40%" stop-color="var(--glass-amber)"/>
            <stop offset="70%" stop-color="var(--glass-blue)"/>
            <stop offset="100%" stop-color="var(--glass-blue)"/>
          </radialGradient>
        </defs>
        <circle cx="130" cy="130" r="128" fill="var(--paper)" stroke="var(--ink)" stroke-width="2"/>
        <circle cx="130" cy="130" r="116" fill="var(--glass-red)" stroke="var(--ink)" stroke-width="2"/>
        <circle cx="130" cy="130" r="104" fill="url(#glass)" stroke="var(--ink)" stroke-width="2"/>
      </svg>
      <div class="volume">600 ml</div>
      <div class="abv">6.9 % vol. alc.</div>
    </div>

    <div class="panel panel--side panel--right">
      <p class="maker">Morvelha fábrica de carvejas especias puro malte come ingredientes celecionados</p>
      <p class="quote">“Na vida, existem outras coisas para além de cervaja, faz essas outras coisas parecerem ainda melhores”</p>
      <div class="body-copy">
        <p>
          <span>Text text texttext text</span>
          <span>Texttext text texttext</span>
          <span>Text texttext text</span>
          <span>Texttext text texttext</span>
          <span>Text texttext text text</span>
        </p>
        <p>
          <span>Text text texttext text</span>
          <span>Texttext text texttext</span>
          <span>Text texttext text</span>
          <span>Texttext text texttext</span>
          <span>Text texttext text text</span>
        </p>
        <p>
          <span>Text text texttext text</span>
          <span>Texttext text texttext</span>
          <span>Text texttext text</span>
        </p>
        <p>
          <span>Texttext text texttext</span>
          <span>Text texttext text text</span>
        </p>
      </div>
    </div>

    <div class="label__rule"></div>
  </section>
</body>
</html>
```